Scuba diving website (Only 1 page. If nice all website later for you)

The payment is for one page only. We are looking for the main design of our new website. For test you will have to redesign the page that is attached to this description. If we like the style we will choose you as the main designer for the whole website (around 20 pages).
The website is about scuba diving. It targets world wide in 4 languages dive centers, divers, underwater photographers, dive sites research, fish species info many more to come. The website is bulid on strong fondation and expect high visits. Developpment is done.
We need now to find the perfect design. The page to redesign is a page about a "dive center" that subscribe to the website where he presents himself and fills it's information. (like a plimbook page).
We are looking for between MODERN and MINIMAL design, but most of all a CLEAN design. See below some design website we like
http://velorint.com/pathe/
http://www.quandrell.com/
http://www.paltravex.com/
http://widgets.tarnimello.com/
For the color stay around the blue and orange. The page width should be 1024px.
Updates
You can use small diving pictures for presenting the "Neighbouring dive sites" in the page. (instead of the red and white flag)
Target Market(s)
We target people willing to go on holiday for diving. We target photographer, cameraman who wants to share picture of their dive, we target people who have an interest for fish species (they can tag more than 32000 different species on their picture/video). We target dive centers who want to advertise on the website by creating their own page

```html
<!DOCTYPE html>
<html lang="en">
<head>
<meta charset="utf-8">
<title>Coral Drift – Scuba Diving Center</title>
<link href="https://fonts.googleapis.com/css2?family=Fira+Sans:ital,wght@0,400;0,500;0,600;1,400&display=swap" rel="stylesheet">
<style>
:root{
  --page:#ffffff;
  --sheet:#e9f3f5;
  --ink:#3c3c3c;
  --text:#111;
  --blue:#2f6fb5;
  --blue-dark:#1d5ea8;
  --btn-blue:#3b7cc2;
  --btn-blue-dark:#2c6199;
  --orange:#f5962a;
  --orange-dark:#d97a14;
  --rule:#5a6a78;
  --box-line:#8fb0c8;
  --star:#f3c531;
}
*{box-sizing:border-box;margin:0;padding:0}
html,body{width:1200px;height:984px;overflow:hidden;background:var(--page);font-family:"Fira Sans",sans-serif}
.sheet{position:absolute;left:108px;top:0;width:984px;height:984px;background:var(--sheet)}
.abs{position:absolute}
.brand{left:124px;top:62px;width:160px;font-size:28px;line-height:34px;font-weight:500;color:#777;display:flex;align-items:center;gap:8px;white-space:nowrap}
.brand-dot{width:16px;height:16px;border-radius:50%;background:#777;flex:none}
.nav a{position:absolute;top:38px;font-size:20px;color:var(--ink);text-decoration:none}
.nav .active{top:0;height:68px;padding:38px 0 0;width:126px;text-align:center;background:linear-gradient(#f8a43c,var(--orange));color:#fff}
.nav-rule{left:296px;top:104px;width:766px;height:1px;background:var(--rule)}
.flag{border-radius:6px;overflow:hidden;box-shadow:0 1px 2px rgba(0,0,0,.35)}
.tab-btn{top:96px;width:88px;height:58px;background:var(--btn-blue);color:#fff;font-size:20px;text-align:center;padding-top:21px;border-radius:0 0 8px 8px;box-shadow:0 2px 3px rgba(0,0,0,.25)}
.tab-btn::after{content:"";position:absolute;right:-15px;top:0;width:15px;height:8px;background:var(--btn-blue-dark);border-radius:0 6px 0 0}
.page-title{left:154px;top:182px;font-size:24px;font-weight:600;color:var(--blue-dark)}
.hero-frame{left:151px;top:232px;width:897px;height:379px;background:#f4f8f9;border:1px solid #d4dde0;box-shadow:0 1px 4px rgba(0,0,0,.25)}
.hero-photo{left:166px;top:245px;width:867px;height:347px;background:radial-gradient(ellipse at 48% 40%,#8fd0f3 0%,#1a86cf 22%,#0b5595 55%,#072a44 100%);box-shadow:1px 2px 3px rgba(0,0,0,.5)}
.center-tag{left:147px;top:259px;width:176px;height:59px;background:var(--orange);color:#fff;font-size:24px;font-style:italic;padding:15px 0 0 20px;box-shadow:1px 2px 3px rgba(0,0,0,.3)}
.center-tag::before{content:"";position:absolute;left:0;top:-10px;width:6px;height:10px;background:var(--orange-dark);border-radius:6px 0 0 0}
.crumbs{left:150px;top:624px;font-size:15px;font-style:italic;color:var(--blue-dark);white-space:nowrap}
.go-back{left:606px;top:625px;font-size:14px;font-style:italic;color:var(--orange);letter-spacing:.5px}
.social{top:620px;height:23px;background:#4a67a8;color:#fff;font-size:14px;font-weight:600;display:flex;align-items:center;gap:4px;padding:0 5px;border:1px solid #3a5490}
.social i{width:14px;height:14px;background:#fff;display:inline-block}
.info-box{left:155px;top:704px;width:892px;height:266px;border:1px solid var(--box-line);border-radius:8px;background:rgba(255,255,255,.35)}
.section-head{font-size:20px;font-weight:400;color:var(--blue);padding-bottom:10px;border-bottom:1px solid var(--rule)}
.row{font-size:15px;font-weight:500;color:var(--text);letter-spacing:.3px;white-space:nowrap}
.row em{color:#5a8fc9;font-weight:400}
.stars{left:780px;display:flex;gap:2px}
.review-btn{left:911px;top:825px;width:147px;height:122px;background:var(--orange);color:#fff;font-size:22px;font-weight:600;text-align:center;line-height:28px;padding-top:38px;box-shadow:1px 2px 4px rgba(0,0,0,.35);border-radius:0 0 4px 4px}
.review-btn::before{content:"";position:absolute;right:0;top:-20px;width:10px;height:20px;background:var(--orange-dark);border-radius:0 8px 0 0}
</style>
</head>
<body>
<svg width="0" height="0" style="position:absolute">
  <defs>
    <symbol id="star" viewBox="0 0 16 16"><polygon points="8,1 10,6 15,6 11,9.5 12.5,15 8,11.8 3.5,15 5,9.5 1,6 6,6" fill="var(--star)" stroke="#c99a1a" stroke-width=".6"/></symbol>
    <symbol id="flag-uk" viewBox="0 0 42 34"><rect width="42" height="34" fill="#23327a"/><path d="M0 0L42 34M42 0L0 34" stroke="#fff" stroke-width="6"/><path d="M0 0L42 34M42 0L0 34" stroke="#c8102e" stroke-width="2"/><path d="M21 0V34M0 17H42" stroke="#fff" stroke-width="10"/><path d="M21 0V34M0 17H42" stroke="#c8102e" stroke-width="6"/></symbol>
    <symbol id="flag-fr" viewBox="0 0 42 34"><rect width="14" height="34" fill="#1f3d99"/><rect x="14" width="14" height="34" fill="#fff"/><rect x="28" width="14" height="34" fill="#e0262e"/></symbol>
    <symbol id="flag-de" viewBox="0 0 42 34"><rect width="42" height="12" fill="#111"/><rect y="12" width="42" height="11" fill="#dd1c1c"/><rect y="23" width="42" height="11" fill="#f5c400"/></symbol>
    <symbol id="flag-es" viewBox="0 0 42 34"><rect width="42" height="34" fill="#d21f1b"/><rect y="9" width="42" height="16" fill="#f7c600"/></symbol>
    <symbol id="flag-cn" viewBox="0 0 30 16"><rect width="30" height="16" fill="#de2910"/><polygon points="6,2 7.2,5 10,5 7.8,7 8.6,10 6,8.2 3.4,10 4.2,7 2,5 4.8,5" fill="#ffde00"/></symbol>
    <symbol id="flag-it" viewBox="0 0 30 16"><rect width="10" height="16" fill="#009246"/><rect x="10" width="10" height="16" fill="#fff"/><rect x="20" width="10" height="16" fill="#ce2b37"/></symbol>
  </defs>
</svg>

<div class="sheet"></div>

<header>
  <div class="abs brand"><span class="brand-dot"></span>Deepward</div>
  <nav class="nav">
    <a style="left:301px">Home</a>
    <a style="left:376px">Latest</a>
    <a style="left:455px">Photos</a>
    <a style="left:537px">Videos</a>
    <a style="left:618px">Fauna</a>
    <a style="left:695px">Dive Site</a>
    <a class="active" style="left:786px">Dive Center</a>
    <a style="left:926px">Divers</a>
    <a style="left:1003px">Forum</a>
  </nav>
  <div class="abs nav-rule"></div>
  <svg class="abs flag" style="left:618px;top:122px" width="42" height="34"><use href="#flag-uk"/></svg>
  <svg class="abs flag" style="left:668px;top:122px" width="42" height="34"><use href="#flag-fr"/></svg>
  <svg class="abs flag" style="left:718px;top:122px" width="42" height="34"><use href="#flag-de"/></svg>
  <svg class="abs flag" style="left:768px;top:122px" width="42" height="34"><use href="#flag-es"/></svg>
  <div class="abs tab-btn" style="left:843px">Sign in</div>
  <div class="abs tab-btn" style="left:959px">Join</div>
</header>

<main>
  <h1 class="abs page-title">Scuba Diving Center</h1>
  <div class="abs hero-frame"></div>
  <div class="abs hero-photo" role="img" aria-label="Two scuba divers silhouetted against sunlit blue water seen from below"></div>
  <div class="abs center-tag">Coral Drift</div>

  <div class="abs crumbs">Home &gt;&gt; Scuba Diving Center &gt;&gt; Indonesia &gt;&gt; Coral Drift</div>
  <div class="abs go-back">&lt;&lt; GO BACK</div>
  <div class="abs social" style="left:937px;width:58px"><i></i>Like</div>
  <div class="abs social" style="left:1001px;width:45px">Share</div>

  <section class="abs info-box"></section>
  <h2 class="abs section-head" style="left:171px;top:731px;width:291px">Main Information</h2>
  <div class="abs row" style="left:171px;top:795px">Location: Indonesia, Bali</div>
  <div class="abs row" style="left:171px;top:830px">Affiliation: <em>NADRA SVT</em></div>
  <div class="abs row" style="left:171px;top:865px">Active since: 2006</div>
  <div class="abs row" style="left:171px;top:899px">Instructor speaks:</div>
  <svg class="abs" style="left:321px;top:900px" width="30" height="16"><use href="#flag-uk"/></svg>
  <svg class="abs" style="left:361px;top:900px" width="24" height="16"><use href="#flag-cn"/></svg>
  <svg class="abs" style="left:395px;top:900px" width="23" height="16"><use href="#flag-it"/></svg>

  <h2 class="abs section-head" style="left:531px;top:729px;width:291px;padding-left:2px">Rating (11 votes)</h2>
  <div class="abs row" style="left:533px;top:793px">Professionalism</div>
  <div class="abs row" style="left:533px;top:828px">Safety</div>
  <div class="abs row" style="left:533px;top:863px">Equipement, air quality</div>
  <div class="abs row" style="left:533px;top:897px">Friendlyness</div>
  <div class="abs row" style="left:533px;top:932px">Price of the service</div>

  <div class="abs stars" style="top:792px"><svg width="16" height="16"><use href="#star"/></svg><svg width="16" height="16"><use href="#star"/></svg><svg width="16" height="16"><use href="#star"/></svg><svg width="16" height="16"><use href="#star"/></svg></div>
  <div class="abs stars" style="top:828px"><svg width="16" height="16"><use href="#star"/></svg><svg width="16" height="16"><use href="#star"/></svg></div>
  <div class="abs stars" style="top:863px"><svg width="16" height="16"><use href="#star"/></svg><svg width="16" height="16"><use href="#star"/></svg><svg width="16" height="16"><use href="#star"/></svg><svg width="16" height="16"><use href="#star"/></svg></div>
  <div class="abs stars" style="top:896px"><svg width="16" height="16"><use href="#star"/></svg><svg width="16" height="16"><use href="#star"/></svg><svg width="16" height="16"><use href="#star"/></svg></div>
  <div class="abs stars" style="top:930px"><svg width="16" height="16"><use href="#star"/></svg><svg width="16" height="16"><use href="#star"/></svg><svg width="16" height="16"><use href="#star"/></svg><svg width="16" height="16"><use href="#star"/></svg></div>

  <div class="abs review-btn">Write<br>a review</div>
</main>
</body>
</html>
```